New ideas for home page of my website

I am looking for some inspiration for my website www.crafteddownriver.com
Most of the content will stay the same but I will be adding on the following new buttons Annual Expo and Awards
Any ideas on alternative layout act will be great. The most creative idea will get the opportunity to pitch for the whole site design.

Colors

Designer to choose colors to be used in the design.

```html
<!DOCTYPE html>
<html lang="en">
<head>
<meta charset="utf-8">
<title>Crafted Downriver – Home</title>
<link href="https://fonts.googleapis.com/css2?family=Open+Sans:wght@400;600;700;800&display=swap" rel="stylesheet">
<style>
:root{
  --red:#c8102e;
  --ink:#2b2b2b;
  --muted:#777;
  --page:#ececec;
  --panel:#ffffff;
  --nav:#e2e2e2;
  --rule:#d4d4d4;
  --footer:#2e2e2e;
  --partner:#f4f4f4;
}
*{box-sizing:border-box;margin:0;padding:0}
html,body{width:783px;height:1200px;overflow:hidden}
body{font-family:"Open Sans",Arial,sans-serif;color:var(--ink);background:var(--page);font-size:9px;position:relative}
.wrap{width:700px;margin:0 auto;position:relative}
.site-header{background:var(--panel);height:72px}
.brand{position:absolute;left:0;top:14px;display:flex;align-items:center;gap:8px}
.brand-mark{width:34px;height:34px;border-radius:50%;background:var(--red)}
.brand-name{font-weight:700;font-size:14px;color:var(--ink);line-height:1}
.header-tools{position:absolute;right:0;top:10px;display:flex;flex-direction:column;align-items:flex-end;gap:6px}
.lang{font-size:8px;color:var(--muted);display:flex;gap:6px;align-items:center}
.lang span.flag{width:14px;height:9px;background:#244a8f;display:inline-block}
.header-actions{display:flex;gap:4px}
.btn-red{background:var(--red);color:#fff;font-weight:700;font-size:8px;padding:5px 9px;border-radius:2px;text-transform:uppercase}
.main-nav{background:var(--nav);height:22px;border-bottom:2px solid var(--rule)}
.main-nav ul{list-style:none;display:flex;height:22px;align-items:center}
.main-nav li{font-size:8px;font-weight:700;padding:0 12px;color:#555;border-right:1px solid #ccc;line-height:10px}
.main-nav li.active{color:var(--red)}
.search{position:absolute;right:0;top:4px;width:120px;height:14px;background:#fff;border:1px solid #ccc;font-size:7px;color:#aaa;padding:1px 5px}
.hero{margin-top:10px;background:var(--panel);height:218px;display:flex;box-shadow:0 1px 3px rgba(0,0,0,.15)}
.hero-photo{width:478px;height:218px;background:linear-gradient(135deg,#7d8a94,#c4b6a2 55%,#8a7a6a)}
.hero-copy{flex:1;padding:26px 18px;text-align:center}
.hero-copy h1{font-size:17px;font-weight:800;line-height:21px;text-transform:uppercase;color:var(--ink)}
.hero-buttons{display:flex;gap:6px;justify-content:center;margin-top:20px}
.btn-dark{background:#333;color:#fff;font-weight:700;font-size:8px;padding:6px 10px;border-radius:2px}
.btn-member{background:var(--red);color:#fff;font-weight:700;font-size:8px;padding:6px 10px;border-radius:2px}
.hero-arrows{display:flex;gap:4px;justify-content:center;margin-top:58px}
.arrow{width:14px;height:14px;border-radius:50%;background:#444;display:flex;align-items:center;justify-content:center}
.dots{text-align:center;margin-top:8px}
.dots span{display:inline-block;width:5px;height:5px;border-radius:50%;background:#bbb;margin:0 2px}
.dots span.on{background:var(--red)}
.section-title{font-size:10px;font-weight:700;color:var(--red);text-transform:uppercase;margin:14px 0 6px;padding-bottom:4px;border-bottom:1px solid var(--rule)}
.card{background:var(--panel);box-shadow:0 1px 3px rgba(0,0,0,.12)}
.featured{display:flex;padding:10px;gap:14px;height:130px;position:relative}
.featured-img{width:240px;height:110px;flex:none;background:linear-gradient(135deg,#8d8d8d,#cfcfcf)}
.featured-body h3{font-size:11px;font-weight:700;line-height:14px;margin-bottom:6px}
.featured-body p{font-size:7px;line-height:10px;color:var(--muted)}
.read{color:var(--red);font-weight:700;font-size:7px;margin-top:6px;display:block}
.members{display:flex;gap:10px;align-items:center;height:44px}
.member{height:40px;flex:1;background:var(--panel);display:flex;align-items:center;justify-content:center;font-weight:700;font-size:10px;color:var(--ink);box-shadow:0 1px 2px rgba(0,0,0,.12)}
.member.dark{background:#1f1f1f;color:#fff}
.member.redbg{background:var(--red);color:#fff}
.lower{display:flex;gap:14px}
.event{width:200px}
.news{flex:1}
.event .card{padding:10px;height:210px}
.event-img{height:60px;background:linear-gradient(135deg,#d9d9d9,#f2f2f2);display:flex;align-items:center;gap:6px;padding:0 10px;font-size:9px;font-weight:700;color:#333}
.event-img i{width:26px;height:26px;border-radius:50%;background:#d28a1a;display:block;flex:none}
.event h4{font-size:10px;font-weight:700;margin:10px 0 4px;line-height:13px}
.event p{font-size:7px;color:var(--muted);line-height:10px}
.news .card{padding:10px;height:210px;display:flex;gap:10px}
.news-item{flex:1;min-width:0}
.news-img{height:70px;background:linear-gradient(135deg,#6a6a6a,#b8b8b8)}
.news-img.plain{background:#1f1f1f}
.news-item h5{font-size:8px;font-weight:700;margin:7px 0 4px;line-height:11px}
.news-item p{font-size:7px;color:var(--muted);line-height:10px}
.partners{position:absolute;left:0;top:890px;width:783px;height:76px;background:var(--partner);border-top:1px solid var(--rule)}
.partners .wrap{display:flex;justify-content:space-between;align-items:center;height:76px;padding:0 30px}
.badge{width:64px;height:22px;background:#d6d6d6;border-radius:3px}
.badge.round{width:28px;height:28px;border-radius:50%}
.stats{position:absolute;left:0;top:966px;width:783px;height:64px;background:var(--red);color:#fff;text-align:center;padding-top:14px}
.stats .line1{font-size:10px;font-weight:600}
.stats .line1 b{font-weight:800}
.stats .line2{font-size:13px;font-weight:700;margin-top:4px}
.site-footer{position:absolute;left:0;top:1030px;width:783px;height:170px;background:var(--footer);color:#bbb}
.site-footer .wrap{display:flex;padding-top:22px}
.f-brand{width:300px}
.f-brand .brand-name{color:#fff;font-size:12px}
.f-brand p{font-size:7px;line-height:10px;margin-top:10px;color:#999}
.f-links{display:flex;gap:40px;flex:1}
.f-col h6{font-size:8px;color:#fff;margin-bottom:4px;height:11px}
.f-col ul{list-style:none}
.f-col li{font-size:7px;line-height:11px}
.social{display:flex;gap:5px;margin-top:6px}
.social span{width:16px;height:16px;border-radius:50%;background:#ddd;display:block}
</style>
</head>
<body>
<header class="site-header">
  <div class="wrap">
    <div class="brand"><span class="brand-mark"></span><span class="brand-name">CRAFTED DOWNRIVER</span></div>
    <div class="header-tools">
      <div class="lang"><span class="flag"></span>ENG ▾</div>
      <div class="header-actions"><span class="btn-red">Annual Expo</span><span class="btn-red">Awards</span></div>
    </div>
  </div>
</header>
<nav class="main-nav">
  <div class="wrap">
    <ul><li class="active">HOME</li><li>LEARN MORE</li><li>NEWS</li><li>EVENTS</li><li>MEMBERS</li><li>COUNCIL</li></ul>
    <div class="search">Search</div>
  </div>
</nav>
<main class="wrap">
  <section class="hero">
    <div class="hero-photo" role="img" aria-label="Photo of two members standing together at an industry event"></div>
    <div class="hero-copy">
      <h1>Championing world class industry in the Downriver</h1>
      <div class="hero-buttons"><span class="btn-member">Become a Member</span><span class="btn-dark">Learn More</span></div>
      <div class="hero-arrows">
        <span class="arrow"><svg width="6" height="8"><path d="M5 0L1 4l4 4" stroke="#fff" fill="none" stroke-width="1.5"/></svg></span>
        <span class="arrow"><svg width="6" height="8"><path d="M1 0l4 4-4 4" stroke="#fff" fill="none" stroke-width="1.5"/></svg></span>
      </div>
    </div>
  </section>
  <div class="dots"><span class="on"></span><span></span><span></span></div>

  <h2 class="section-title">Featured Articles</h2>
  <article class="card featured">
    <div class="featured-img" role="img" aria-label="Photo of engineers reviewing product designs"></div>
    <div class="featured-body">
      <h3>Product Lifecycle Management webinars demonstrate benefits to SMEs</h3>
      <p>Product lifecycle management tools are no longer just for large manufacturers. Our free webinar series shows small and medium firms how shared data, design control and smarter workflows cut costs, shorten lead times and help teams bring better products to market faster than ever before.</p>
      <span class="read">READ FULL ARTICLE »</span>
    </div>
  </article>

  <h2 class="section-title">Latest Members</h2>
  <div class="members">
    <div class="member dark">Kestrel Moulding</div>
    <div class="member redbg">Atlas</div>
    <div class="member">Norvale</div>
    <div class="member dark">Thornbury &amp; Co</div>
    <div class="member redbg">Pellmark</div>
  </div>

  <div class="lower">
    <section class="event">
      <h2 class="section-title">Upcoming Event</h2>
      <div class="card">
        <div class="event-img"><i></i>Riverside Enterprise Centre</div>
        <h4>Crafted Downriver 2014 Exhibition</h4>
        <p>Riverside Racecourse<br>10:00 to 16:00</p>
        <span class="btn-red" style="display:inline-block;margin-top:10px">Register Now »</span>
      </div>
    </section>
    <section class="news">
      <h2 class="section-title">Latest News</h2>
      <div class="card">
        <div class="news-item">
          <div class="news-img plain" role="img" aria-label="Advisory group banner image"></div>
          <h5>Stand out from the crowd: it's time to shine…</h5>
          <p>By Makers Advisory Group</p>
        </div>
        <div class="news-item">
          <div class="news-img" role="img" aria-label="Photo of a machining workshop"></div>
          <h5>Ashby &amp; Crane to Launch New Product Ranges at Expo</h5>
          <p>By Ashby &amp; Crane Ltd</p>
        </div>
        <div class="news-item">
          <div class="news-img" role="img" aria-label="Photo of a factory production line"></div>
          <h5>Local plant expands with new skilled jobs</h5>
          <p>By Norvale</p>
        </div>
      </div>
    </section>
  </div>
</main>

<div class="partners"><div class="wrap">
  <span class="badge round"></span><span class="badge"></span><span class="badge"></span><span class="badge round"></span><span class="badge"></span><span class="badge"></span>
</div></div>

<section class="stats">
  <div class="line1">MANUFACTURING STATS: <b>32,000 companies / 600,000 employees</b></div>
  <div class="line2">The birthplace of the industrial revolution and pioneers in advanced manufacturing</div>
</section>

<footer class="site-footer"><div class="wrap">
  <div class="f-brand">
    <div class="brand" style="position:static"><span class="brand-mark" style="width:24px;height:24px"></span><span class="brand-name">CRAFTED DOWNRIVER</span></div>
    <p>© 2014 Crafted Downriver. All Rights Reserved<br>www.crafteddownriver.com · Privacy</p>
  </div>
  <div class="f-links">
    <div class="f-col"><h6>Links</h6><ul><li>Home</li><li>About Us</li><li>Learn more</li><li>News</li><li>Members</li></ul></div>
    <div class="f-col"><h6></h6><ul><li>Contact Us</li><li>Blog</li><li>Terms &amp; Conditions</li></ul></div>
    <div class="f-col"><h6>Connect Us</h6><div class="social"><span></span><span></span><span></span><span></span></div></div>
  </div>
</div></footer>
</body>
</html>
```